Business Card for Lumina Nest

I need a very attractive business card as per the logo..

lumina nest is a centre providing services to pregnant women...

DR. Karim Haddadi

Consultant-  Maternal Fetal Medicine & Director of Lumina Nest Center

Kingdom of Saudi Arabia

Tel : +966 1 57 3 8164

Fax : +966 1 57 3 9275

khaddadi@luminest-example.com

www.luminanest-example.com

Target Market(s)

the target market is the pregnant women and women having issues with pregnancy or with babies

Industry/Entity Type

Business

Requirements
Must have
• the business card will be in English and Arabic..........one we finalize the design maybe on the back u can place Arabic..of in the front one side may be Arabic one side english

```html
<!DOCTYPE html>
<html lang="en">
<head>
<meta charset="utf-8">
<title>Lumina Nest – Business Card</title>
<link rel="stylesheet" href="https://fonts.googleapis.com/css2?family=Roboto+Condensed:wght@300;400&display=swap">
<style>
  :root {
    --teal: #6ec8b6;
    --ink: #4a4a4a;
    --ink-soft: #7a7a7a;
    --frame: #7d7d7d;
    --white: #ffffff;
  }
  * { margin: 0; padding: 0; box-sizing: border-box; }
  html, body { width: 904px; height: 1200px; overflow: hidden; background: var(--white); }
  body { position: relative; font-family: "Roboto Condensed", "Arial Narrow", sans-serif; }

  .card { position: absolute; width: 628px; height: 388px; overflow: hidden; }
  .card--front { left: 129px; top: 147px; border: 2px solid var(--frame); background: var(--white); }
  .card--back { left: 127px; top: 649px; background: var(--teal); }

  .brand { position: absolute; left: 98px; top: 122px; display: flex; align-items: center; gap: 22px; }
  .brand__dot { width: 110px; height: 110px; border-radius: 50%; border: 8px solid var(--teal); }
  .card--back .brand__dot { border-color: var(--white); }
  .brand__name { font-weight: 400; font-size: 62px; line-height: 1; color: var(--teal); letter-spacing: 0.5px; }
  .card--back .brand__name { color: var(--white); }

  .person { position: absolute; left: 229px; top: 235px; width: 350px; }
  .person__name { font-size: 19px; font-weight: 400; color: var(--ink); padding-bottom: 1px; border-bottom: 1px solid #9a9a9a; }
  .card--back .person__name { color: #3d3d3d; border-bottom-color: #4f6e68; }

  .person__body { display: grid; grid-template-columns: 176px 1fr; padding-top: 4px; }
  .role { font-size: 14.5px; font-weight: 300; line-height: 24px; color: var(--ink-soft); white-space: nowrap; }
  .role__title { font-weight: 400; color: var(--ink); }
  .card--back .role__title { color: #3d3d3d; }

  .contact { list-style: none; }
  .contact li { display: flex; align-items: center; gap: 8px; font-size: 13px; font-weight: 300; line-height: 24px; color: var(--ink-soft); white-space: nowrap; }
  .card--back .contact li { color: var(--white); }
  .contact svg { width: 13px; height: 13px; flex: none; fill: #4a4a4a; }
</style>
</head>
<body>

<section class="card card--front">
  <div class="brand">
    <span class="brand__dot"></span>
    <span class="brand__name">Lumina Nest</span>
  </div>
  <div class="person">
    <h1 class="person__name">Dr. Karim Haddadi</h1>
    <div class="person__body">
      <div class="role">
        <div class="role__title">Consultant</div>
        <div>Maternal Fetal Medicine &amp;</div>
        <div>Director of Lumina Nest Center</div>
        <div>Kingdom of Saudi Arabia</div>
      </div>
      <ul class="contact">
        <li><svg viewBox="0 0 14 14"><path d="M1 2h3v11H1zM5 3h8v10H5zm1.5 2v1.5h5V5zm0 3v1.2h1.2V8zm2 0v1.2h1.2V8zm2 0v1.2h1.2V8zm-4 2v1.2h1.2V10zm2 0v1.2h1.2V10zm2 0v1.2h1.2V10z"/></svg>+966 1 57 3 8164</li>
        <li><svg viewBox="0 0 14 14"><path d="M3 1h8v3H3zM1 5h12v5h-2V8H3v2H1zm3 4h6v4H4z"/></svg>+966 1 57 3 9275</li>
        <li><svg viewBox="0 0 14 14"><path d="M10 1l3 3-8 8-4 1 1-4zM2.6 9.6l-.5 2.3 2.3-.5z"/></svg>khaddadi@luminest-example.com</li>
        <li><svg viewBox="0 0 14 14"><path d="M1 2h12v8H1zm1.5 1.5v5h9v-5zM5 11h4v1h2v1H3v-1h2z"/></svg>www.luminanest-example.com</li>
      </ul>
    </div>
  </div>
</section>

<section class="card card--back">
  <div class="brand">
    <span class="brand__dot"></span>
    <span class="brand__name">Lumina Nest</span>
  </div>
  <div class="person">
    <h2 class="person__name">Dr. Karim Haddadi</h2>
    <div class="person__body">
      <div class="role">
        <div class="role__title">info in arabic</div>
      </div>
      <ul class="contact">
        <li><svg viewBox="0 0 14 14"><path d="M1 2h3v11H1zM5 3h8v10H5zm1.5 2v1.5h5V5zm0 3v1.2h1.2V8zm2 0v1.2h1.2V8zm2 0v1.2h1.2V8zm-4 2v1.2h1.2V10zm2 0v1.2h1.2V10zm2 0v1.2h1.2V10z"/></svg>+966 1 57 3 8164</li>
        <li><svg viewBox="0 0 14 14"><path d="M3 1h8v3H3zM1 5h12v5h-2V8H3v2H1zm3 4h6v4H4z"/></svg>+966 1 57 3 9275</li>
        <li><svg viewBox="0 0 14 14"><path d="M10 1l3 3-8 8-4 1 1-4zM2.6 9.6l-.5 2.3 2.3-.5z"/></svg>khaddadi@luminest-example.com</li>
        <li><svg viewBox="0 0 14 14"><path d="M1 2h12v8H1zm1.5 1.5v5h9v-5zM5 11h4v1h2v1H3v-1h2z"/></svg>www.luminanest-example.com</li>
      </ul>
    </div>
  </div>
</section>

</body>
</html>
```